8"x5" postcard for Wireless Internet introduction to new mountain town market

I need to market high speed internet to a resort mountain town without doing the obvious laptop on a mountain top thing, so tired. We are going to be competing directly with another provider with same cost, but we will be offering free installation. The area is Aspen Colorado, so the clientele are outdoor types who have suffered for years from being disconnected in their mountain town. We offer fast internet and excellent customer service from people who live in their neck of the woods.

Target Market(s)

23-55 years old, both resort living, families and ski bums

Font styles to use
Sans Serif

Colors

Designer to choose colors to be used in the design.

Requirements
Must have
• Visual appeal and fresh verbiage. We don't mind being a little edgy. We are a young company and we want to appeal to people looking for a provider who gets them. We prefer a clean look.
Nice to have
• Nice to have colors that match our logo
Should not have
• stuffy concepts or verbiage that is too much like a car salesman. We don't want to look like a 'big box' company.

```html
<!DOCTYPE html>
<html lang="en">
<head>
<meta charset="utf-8">
<title>Summit Line Broadband – Postcard</title>
<link rel="stylesheet" href="https://fonts.googleapis.com/css2?family=Anton&family=Oswald:wght@700&family=Permanent+Marker&family=Montserrat:wght@600;800&display=swap">
<style>
  :root{
    --orange:#f7931e;
    --orange-deep:#f26b1d;
    --yellow:#ffc629;
    --yellow-soft:#ffd65a;
    --ink:#161616;
    --red:#e3241b;
    --white:#ffffff;
    --photo-light:#e9e4df;
    --photo-mid:#b9a79a;
    --photo-dark:#6d5546;
    --logo-text:#3a3a3a;
  }
  *{margin:0;padding:0;box-sizing:border-box}
  html,body{width:851px;height:1200px;overflow:hidden;background:var(--white)}
  .postcard{position:relative;width:851px;height:1200px;overflow:hidden;
    background:linear-gradient(160deg,var(--yellow-soft) 0%,var(--orange) 55%,var(--orange-deep) 100%);}
  .hero-photo{position:absolute;left:0;top:0;width:851px;height:640px;
    background:radial-gradient(ellipse at 40% 35%,var(--photo-mid) 0%,var(--photo-dark) 30%,var(--photo-light) 60%,var(--white) 100%);}
  .accents{position:absolute;left:0;top:0}
  .logo{position:absolute;top:34px;right:44px;display:flex;align-items:center;gap:12px;
    background:var(--white);padding:10px 16px;}
  .logo-mark{width:30px;height:30px;border-radius:50%;background:var(--orange)}
  .logo-name{font:800 22px/1 'Montserrat',sans-serif;color:var(--logo-text);letter-spacing:.5px}
  .headline{position:absolute;left:0;width:100%;top:478px;text-align:center;
    font:400 66px/1 'Anton',sans-serif;color:var(--ink);letter-spacing:1px;
    transform:skewX(-12deg);-webkit-text-stroke:2px var(--yellow);
    text-shadow:3px 3px 0 var(--yellow);}
  .tagline-band{position:absolute;left:0;top:566px;width:851px;height:72px;background:var(--white);
    display:flex;align-items:center;justify-content:center;}
  .tagline{font:700 46px/1 'Oswald',sans-serif;color:var(--ink);letter-spacing:.5px}
  .offer-band{position:absolute;left:0;top:0}
  .offer{position:absolute;left:0;width:100%;top:740px;text-align:center;
    font:400 60px/1.15 'Permanent Marker',sans-serif;color:var(--red);}
  .pitch{position:absolute;left:70px;right:70px;top:955px;text-align:center;
    font:800 29px/1.25 'Montserrat',sans-serif;color:var(--ink);}
  .contacts{position:absolute;left:0;right:0;top:1112px;display:flex;justify-content:center;gap:28px;
    font:600 12px/1 'Montserrat',sans-serif;color:var(--ink);}
  .contact{display:flex;align-items:center;gap:7px}
  .contact svg{width:20px;height:20px;flex:none}
</style>
</head>
<body>
<main class="postcard">
  <div class="hero-photo" role="img" aria-label="Smiling young woman with curly hair looking at her smartphone, overlaid with faint hexagon network graphics"></div>

  <svg class="accents" width="851" height="640" viewBox="0 0 851 640" aria-hidden="true">
    <polygon points="0,0 260,0 0,150" fill="var(--orange)"/>
    <polygon points="600,0 851,0 851,130" fill="var(--yellow)" opacity=".85"/>
    <polygon points="0,420 851,330 851,566 0,566" fill="var(--orange)" opacity=".55"/>
    <polygon points="0,470 851,400 851,566 0,566" fill="var(--yellow)" opacity=".75"/>
  </svg>

  <div class="logo">
    <span class="logo-mark"></span>
    <span class="logo-name">SUMMIT LINE BROADBAND</span>
  </div>

  <h1 class="headline">SUPER FAST INTERNET</h1>

  <div class="tagline-band"><p class="tagline">WE ARE BETTER, NOT BIGGER!</p></div>

  <svg class="offer-band" width="851" height="1200" viewBox="0 0 851 1200" aria-hidden="true">
    <polygon points="0,700 851,650 851,760 0,820" fill="var(--yellow-soft)" opacity=".45"/>
    <path d="M150,725 Q400,700 700,718 L690,880 Q420,900 165,875 Z" fill="var(--white)"/>
  </svg>

  <p class="offer">FREE<br>INSTALLATION</p>

  <p class="pitch">We offer fast internet and excellent customer service from people who live in their neck of the woods</p>

  <footer class="contacts">
    <span class="contact">
      <svg viewBox="0 0 20 20"><circle cx="10" cy="10" r="10" fill="var(--orange-deep)"/><rect x="5" y="6.5" width="10" height="7" fill="none" stroke="#fff" stroke-width="1.3"/><path d="M5 6.5 L10 10.5 L15 6.5" fill="none" stroke="#fff" stroke-width="1.3"/></svg>
      hello@summitlinebb.com
    </span>
    <span class="contact">
      <svg viewBox="0 0 20 20"><circle cx="10" cy="10" r="10" fill="var(--orange-deep)"/><path d="M7 5 L9 8 L8 9.5 Q9 11.5 10.5 12 L12 11 L15 13 L13.5 15 Q8 14.5 5.5 7 Z" fill="#fff"/></svg>
      970.555.0142
    </span>
    <span class="contact">
      <svg viewBox="0 0 20 20"><circle cx="10" cy="10" r="10" fill="var(--orange-deep)"/><circle cx="10" cy="10" r="5" fill="none" stroke="#fff" stroke-width="1.2"/><path d="M5 10 H15 M10 5 Q7 10 10 15 M10 5 Q13 10 10 15" fill="none" stroke="#fff" stroke-width="1"/></svg>
      www.summitlinebb.com
    </span>
    <span class="contact">
      <svg viewBox="0 0 20 20"><circle cx="10" cy="10" r="10" fill="var(--orange-deep)"/><circle cx="10" cy="8" r="2.5" fill="#fff"/><path d="M5.5 15 Q10 9.5 14.5 15 Z" fill="#fff"/></svg>
      /summitlinebb
    </span>
  </footer>
</main>
</body>
</html>
```